Interior Design Company - Project Folder Design

Require simple layout design for company folders in a specific template as attach. Company name is MOVALT. Tag line is "make our visions alive, lasting, timeless" in Microsoft Word <Juice ITC> font type. Corporate colors include dark grey, turqoise and white.
Logo, AI template and some images are attached.

Company focus on Interior Design and Build services. Our services includes all commercial and residential projects.

Target Market(s)

B2B,B2C Corporate and Residential Design, Fit-outs and Project Management

Industry/Entity Type

Interior

Font styles to use
Sans Serif

Colors
33a6d7
333333
ffffff

Requirements
Must have
• Logo
• Address - No. 58 Kerrow Lane #04-21, Danvel Centre, Singapore 177492
• Web - www.movalt.com
Nice to have
• Clean professional architectural lines
Should not have
• No cartoons, kiddy images nor repetitive patterns

```html
<!DOCTYPE html>
<html lang="en">
<head>
<meta charset="utf-8">
<title>MOVALT – Quotation Folder</title>
<link rel="stylesheet" href="https://fonts.googleapis.com/css2?family=Open+Sans:wght@300;400;700&family=Pompiere&display=swap">
<style>
  :root{
    --backdrop:#dedede;
    --turquoise:#2ba3d8;
    --ink:#050505;
    --white:#ffffff;
    --dieline:#d23a4e;
    --muted:#9a9a9a;
    --partner:#1f3f9a;
    --badge:#f0901c;
  }
  html,body{margin:0;padding:0;overflow:hidden}
  body{width:1200px;height:818px;background:var(--backdrop);position:relative;font-family:"Open Sans",sans-serif}
  .folder-art{position:absolute;left:0;top:0}
  .brand-name{position:absolute;color:var(--white);font-weight:300;letter-spacing:.5px;line-height:1}
  .brand-name--flap{left:216px;top:408px;font-size:19px;transform:translateX(-50%)}
  .brand-name--back{left:309px;top:614px;font-size:14px}
  .brand-name--front{left:1028px;top:577px;font-size:32px;transform:translateX(-50%)}
  .studio-address{position:absolute;left:309px;top:637px;font-size:7px;line-height:9px;color:var(--muted)}
  .tagline{position:absolute;right:122px;top:630px;font-family:"Pompiere",cursive;font-size:24px;color:var(--white);white-space:nowrap}
  .partner-name{position:absolute;left:760px;top:152px;font-weight:700;font-size:19px;line-height:20px;color:var(--partner);letter-spacing:1px}
  .partner-mark{position:absolute;left:734px;top:151px;width:20px;height:20px;background:var(--partner)}
  .spine-label{position:absolute;left:707px;font-size:5px;letter-spacing:1.6px;color:var(--white);writing-mode:vertical-rl;white-space:nowrap}
  .spine-label--top{top:165px}
  .spine-label--bottom{top:598px}
</style>
</head>
<body>
<svg class="folder-art" width="1200" height="818" viewBox="0 0 1200 818" aria-hidden="false">
  <defs>
    <linearGradient id="warmRoom" x1="0" y1="0" x2="1" y2="1">
      <stop offset="0" stop-color="#8a7a62"/><stop offset=".5" stop-color="#c9b596"/><stop offset="1" stop-color="#4a3d2e"/>
    </linearGradient>
    <linearGradient id="greyRoom" x1="0" y1="0" x2="1" y2="1">
      <stop offset="0" stop-color="#f2f2f2"/><stop offset=".6" stop-color="#b9b9b9"/><stop offset="1" stop-color="#6a6a6a"/>
    </linearGradient>
    <linearGradient id="goldRoom" x1="0" y1="0" x2="1" y2="1">
      <stop offset="0" stop-color="#d8cdb5"/><stop offset=".5" stop-color="#8d7550"/><stop offset="1" stop-color="#3a2f22"/>
    </linearGradient>
  </defs>

  <!-- side flap -->
  <rect class="flap" x="67" y="83" width="200" height="652" fill="var(--turquoise)"/>
  <rect class="flap-strip" x="267" y="126" width="15" height="567" fill="var(--turquoise)"/>

  <!-- front & back interiors -->
  <g class="interior-panels">
    <rect x="282" y="126" width="851" height="567" fill="url(#warmRoom)" role="img" aria-label="Living room interior with television wall and glass coffee table"/>
    <polygon points="400,126 1000,126 700,513" fill="url(#greyRoom)" role="img" aria-label="Bright apartment hallway with framed art and crystal chandelier"/>
    <polygon points="1000,126 1133,126 1133,560 860,693 700,693 700,513" fill="url(#goldRoom)" role="img" aria-label="Dining room with cream chairs and golden chandelier"/>
  </g>

  <!-- dark geometric fields -->
  <polygon class="field" points="206,336 496,693 67,693 67,472" fill="var(--ink)"/>
  <rect class="field" x="67" y="693" width="200" height="41" fill="var(--ink)"/>
  <polygon class="field" points="1012,500 1133,588 1133,693 792,693" fill="var(--ink)"/>

  <!-- partner badge -->
  <circle class="badge" cx="1013" cy="460" r="54" fill="var(--badge)"/>

  <!-- dieline -->
  <g class="dieline" fill="none" stroke="var(--dieline)" stroke-width=".8">
    <rect x="67" y="83" width="200" height="652"/>
    <line x1="67" y1="111" x2="267" y2="111"/>
    <line x1="67" y1="126" x2="267" y2="126"/>
    <line x1="67" y1="693" x2="267" y2="693"/>
    <line x1="67" y1="708" x2="267" y2="708"/>
    <line x1="74" y1="111" x2="67" y2="92"/><line x1="260" y1="111" x2="267" y2="92"/>
    <line x1="74" y1="708" x2="67" y2="728"/><line x1="260" y1="708" x2="267" y2="728"/>
    <rect x="282" y="126" width="851" height="567"/>
    <line x1="701" y1="126" x2="701" y2="693"/>
    <line x1="709" y1="126" x2="709" y2="693"/>
    <path d="M86 580 Q100 605 86 632"/>
    <path d="M182 580 Q160 605 176 632"/>
    <path d="M252 580 Q232 605 252 632"/>
    <path d="M130 658 Q160 638 200 658"/>
  </g>
</svg>

<span class="brand-name brand-name--flap">movalt</span>

<span class="brand-name brand-name--back">movalt</span>
<p class="studio-address" style="margin:0">No. 58 Kerrow Lane #04-21,<br>Danvel Centre, Singapore 177492<br>www.movalt.com</p>

<span class="spine-label spine-label--top">Kestrel Coatings Preferred Designers</span>
<span class="spine-label spine-label--bottom">Quotation Folder</span>

<span class="partner-mark"></span>
<span class="partner-name">KESTREL<br>COATINGS</span>

<span class="brand-name brand-name--front">movalt</span>
<span class="tagline">make our visions alive, lasting, timeless</span>
</body>
</html>
```